Business Card Design

Two women who are flipping houses. Want the women with sledge hammers and in work boots. Liked the ones for cleaning with the woman but just needs some modifications to the women. On the back, I want both of our names and phone numbers.

Rosalind Halvorsen
214-803-5127

Bettina Halvorsen
312-908-2741

Business

NAILED IT TWICE!!!!

```html
<!DOCTYPE html>
<html lang="en">
<head>
<meta charset="utf-8">
<title>Business Card – Nailed It Twice</title>
<link rel="stylesheet" href="https://fonts.googleapis.com/css2?family=Cinzel:wght@500&family=Tinos&display=swap">
<style>
  :root {
    --navy: #1b4876;
    --yellow: #fbe51b;
    --white: #ffffff;
    --ink: #1a1a1a;
    --backdrop: #e4e4e4;
    --photo-light: #b9c0c8;
    --photo-dark: #4a5a72;
  }
  html, body {
    margin: 0;
    padding: 0;
    width: 1200px;
    height: 985px;
    overflow: hidden;
    background: var(--backdrop);
  }
  .stage {
    position: relative;
    width: 1200px;
    height: 985px;
  }
  .card {
    position: absolute;
    width: 620px;
    height: 354px;
    border-radius: 22px;
    overflow: hidden;
    background: var(--white);
    box-shadow: 0 6px 18px rgba(0,0,0,0.18);
  }
  .card--contacts { left: 110px; top: 110px; }
  .card--cover    { left: 470px; top: 520px; }
  .card svg { display: block; width: 100%; height: 100%; }
  .slogan {
    font-family: "Cinzel", serif;
    font-size: 17px;
    letter-spacing: 1px;
    fill: var(--white);
  }
  .contact-list {
    position: absolute;
    left: 372px;
    top: 112px;
    margin: 0;
    font-family: "Tinos", serif;
    font-size: 21px;
    line-height: 1.05;
    letter-spacing: 1.5px;
  }
  .contact { margin: 0 0 16px; }
  .contact-name { color: var(--navy); display: block; }
  .contact-phone { color: var(--ink); display: block; }
</style>
</head>
<body>
<main class="stage">

  <!-- Back of card: names and phone numbers -->
  <section class="card card--contacts">
    <svg viewBox="0 0 620 354" aria-hidden="false">
      <defs>
        <linearGradient id="workerToneA" x1="0" y1="0" x2="0" y2="1">
          <stop offset="0" stop-color="var(--photo-light)"/>
          <stop offset="1" stop-color="var(--photo-dark)"/>
        </linearGradient>
      </defs>
      <polygon class="panel-navy" points="0,0 312,0 312,95 250,354 0,354" fill="var(--navy)"/>
      <polygon class="panel-yellow" points="95,354 225,225 338,268 300,354" fill="var(--yellow)"/>
      <rect class="corner-mark" x="6" y="8" width="16" height="16" fill="var(--yellow)"/>
      <rect class="corner-mark" x="6" y="330" width="16" height="16" fill="var(--yellow)"/>
      <text class="slogan" transform="translate(21,318) rotate(-90)">NAILED IT TWICE!!!!</text>
      <rect class="worker-photo" x="80" y="28" width="150" height="300" rx="4"
            fill="url(#workerToneA)" role="img"
            aria-label="Photo of a woman in a hard hat, plaid shirt, jeans and work boots holding a sledgehammer"/>
    </svg>
    <div class="contact-list">
      <p class="contact">
        <span class="contact-name">Rosalind Halvorsen</span>
        <span class="contact-phone">214-803-5127</span>
      </p>
      <p class="contact">
        <span class="contact-name">Bettina Halvorsen</span>
        <span class="contact-phone">312-908-2741</span>
      </p>
    </div>
  </section>

  <!-- Front of card: slogan and worker photo -->
  <section class="card card--cover">
    <svg viewBox="0 0 620 354" aria-hidden="false">
      <defs>
        <linearGradient id="workerToneB" x1="0" y1="0" x2="0" y2="1">
          <stop offset="0" stop-color="var(--photo-light)"/>
          <stop offset="1" stop-color="var(--photo-dark)"/>
        </linearGradient>
      </defs>
      <rect class="slogan-band" x="0" y="0" width="44" height="354" fill="var(--navy)"/>
      <rect class="corner-mark" x="24" y="6" width="16" height="16" fill="var(--yellow)"/>
      <rect class="corner-mark" x="4" y="332" width="16" height="16" fill="var(--yellow)"/>
      <text class="slogan" transform="translate(30,318) rotate(-90)">NAILED IT TWICE!!!!</text>
      <polygon class="block-navy" points="372,168 620,148 620,282 402,300" fill="var(--navy)"/>
      <polygon class="block-navy" points="300,354 620,354 620,298 392,314" fill="var(--navy)"/>
      <polygon class="block-yellow" points="165,296 418,212 462,322 260,354 220,354" fill="var(--yellow)"/>
      <rect class="worker-photo" x="80" y="24" width="170" height="300" rx="4"
            fill="url(#workerToneB)" role="img"
            aria-label="Photo of a woman in a hard hat, plaid shirt, jeans and work boots holding a sledgehammer"/>
    </svg>
  </section>

</main>
</body>
</html>
```